Redesign This Psychology Website

We would like a slight redesign of this successful psychology (relationship counselling) website:

www.TheLumaHaven.com.au

We are updating the website, and we'd like a slight refresh of the design and style.

Please keep to very similar colours, and use the same logo. We're looking for around 10 page templates, however the main one is the home page.

Keep in mind, this website already converts quite well, so we want a new, fresh design in keeping with this one. Please don't bother designing something too extremely different.

thanks :)
Updates

Target Market(s)

couples who are looking for relationship counselling. Men and women, 25 - 70, across Australia

Industry/Entity Type

Psychology

Number of Pages Required

5+ page

Font styles to use
Sans Serif

Colors
87cfc6
b7a5cd
ec1f27
ffffff
cee9f5

Requirements
Must have
• a similar look to the current design, just looking for a slight refresh.
• Search bar
• Areas for lots of photos
• same logo
• lots of content areas
Nice to have
• great content areas, where we can display a lot of content and our areas.
Should not have
• no colors like orange, etc.
• should not have a totally different feel.

```html
<!DOCTYPE html>
<html lang="en">
<head>
<meta charset="utf-8">
<title>Luma Haven – Relationship &amp; Marriage Counselling</title>
<link href="https://fonts.googleapis.com/css2?family=Open+Sans:wght@300;400;600;700&display=swap" rel="stylesheet">
<style>
:root{
  --teal:#87cfc6;
  --teal-dark:#4fb3a6;
  --purple:#b7a5cd;
  --purple-dark:#7d63a8;
  --red:#ec1f27;
  --green:#5e9a2e;
  --sky:#cee9f5;
  --white:#ffffff;
  --ink:#444444;
  --muted:#8a8a8a;
  --line:#e3e3e3;
  --bar:#efefef;
}
*{box-sizing:border-box;margin:0;padding:0}
html,body{width:1200px;height:4369px;overflow:hidden}
body{font-family:"Open Sans",Arial,sans-serif;color:var(--ink);background:var(--white);font-size:13px;line-height:1.5;position:relative}
a{color:inherit;text-decoration:none}
.wrap{width:966px;margin:0 auto;position:relative}

/* top bar */
.topbar{height:40px;background:var(--bar);font-size:12px}
.topbar .wrap{display:flex;justify-content:space-between;align-items:center;height:40px}
.toplinks{display:flex}
.toplinks a{padding:0 12px;border-left:1px solid #cfcfcf}
.toplinks a:first-child{border-left:0}

/* header */
.header{height:120px}
.header .wrap{height:120px;display:flex;align-items:center}
.brand{display:flex;align-items:center;gap:10px;width:365px}
.brand-dot{width:38px;height:38px;border-radius:50%;background:var(--teal-dark);flex:none}
.brand-name{font-size:30px;font-weight:400;color:var(--teal-dark);line-height:1}
.search{width:335px;height:40px;border:1px solid #ccc;border-radius:3px;display:flex;align-items:center;padding:0 10px;gap:8px;color:#999;font-size:12px}
.callus{margin-left:auto;text-align:right}
.callus small{display:block;color:var(--teal-dark);font-size:13px}
.callus b{font-size:25px;color:var(--red);font-weight:600;display:flex;align-items:center;gap:8px}

/* nav */
.nav{height:65px;background:linear-gradient(180deg,#9fdad2,var(--teal))}
.nav .wrap{display:flex;height:65px;align-items:center}
.nav a{color:#fff;font-weight:700;font-size:15px;text-transform:uppercase;line-height:1.15;padding:0 14px;border-left:1px solid rgba(255,255,255,.6)}
.nav a:first-child{padding-left:0;border-left:0}

/* hero */
.hero{height:517px;position:relative;background:linear-gradient(120deg,#6e8a3a 0%,#a9b86a 35%,#c9a48a 55%,#7a8d45 100%)}
.hero-title{position:absolute;left:117px;top:280px;color:#fff;font-size:38px;font-weight:600;line-height:1.2;letter-spacing:.5px}
.finder{position:absolute;left:757px;top:95px;width:296px;height:355px;background:rgba(155,130,190,.88);padding:22px 22px;color:#fff}
.finder h3{text-align:center;font-size:21px;font-weight:600;line-height:1.2;padding-bottom:14px;border-bottom:1px solid rgba(255,255,255,.6);margin-bottom:12px}
.finder label{display:block;font-size:12px;margin:8px 0 4px}
.finder .field{height:30px;background:#fff;font-size:11px;color:#777;padding:6px 10px;display:flex;justify-content:space-between}
.finder .go{margin-top:16px;height:34px;background:var(--red);text-align:center;font-weight:700;line-height:34px;font-size:15px}
.dots{position:absolute;top:470px;left:0;right:0;display:flex;justify-content:center;gap:10px}
.dots i{width:12px;height:12px;border-radius:50%;background:#fff;opacity:.95}
.dots i:first-child{background:transparent;border:2px solid #fff}

/* intro */
.intro{height:378px;position:relative}
.video{position:absolute;left:140px;top:35px;width:436px;height:270px;background:linear-gradient(135deg,#d8c7bd,#b9a69a 50%,#8d8a95);display:flex;align-items:center;justify-content:center}
.intro-text{position:absolute;left:617px;top:40px;width:450px}
.intro-text h2{font-size:30px;font-weight:400;color:#333;line-height:1.2;margin-bottom:18px}
.intro-text p{font-size:13.5px;color:#666;line-height:1.7}
.divider{position:absolute;left:130px;right:130px;bottom:12px;border-top:1px solid var(--line)}
.divider svg{position:absolute;left:50%;top:-1px;transform:translateX(-50%)}

/* service cards */
.services{height:383px}
.cards{display:flex;gap:13px;padding-top:36px;margin-left:13px}
.card{width:227px;height:343px;border:1px solid var(--line);background:#fff}
.card .ph{height:166px}
.card .body{padding:14px 18px}
.card h4{font-size:18px;font-weight:400;line-height:1.2;margin-bottom:8px}
.card p{font-size:10px;color:var(--muted);line-height:1.45;height:54px}
.btn{display:inline-block;color:#fff;font-size:11px;padding:5px 18px;margin-top:10px}

/* band */
.band{height:466px;position:relative;background:linear-gradient(100deg,var(--purple) 0%,#a99bc8 45%,var(--teal) 100%);overflow:hidden}
.band-photo{position:absolute;right:0;top:0;width:500px;height:466px;clip-path:polygon(32% 0,100% 0,100% 100%,0 100%);background:linear-gradient(135deg,#a8c8e0,#e0cdb8 50%,#c9b39c)}
.band h2{position:absolute;left:130px;top:75px;color:#fff;font-size:30px;font-weight:400}
.band .sub{position:absolute;left:130px;top:122px;color:#fff;font-size:17px}
.band ul{position:absolute;top:175px;list-style:none;color:#fff;font-size:14.5px}
.band li{height:35px;display:flex;align-items:center;gap:8px}
.band li::before{content:"›";font-weight:700}

/* approach */
.approach{height:851px;position:relative}
.col-main{position:absolute;left:130px;top:55px;width:585px}
.col-main h2{font-size:24px;font-weight:400;line-height:1.2;margin-bottom:14px}
.col-main p{font-size:12.5px;color:#666;line-height:1.6;margin-bottom:12px}
.h-red{color:var(--red)}
.h-purple{color:var(--purple-dark)}
.h-teal{color:var(--teal-dark)}
.loc{display:grid;grid-template-columns:175px 175px 175px;font-size:12px;color:#555;row-gap:8px;margin-bottom:40px}
.side{position:absolute;left:762px;width:308px;height:236px;border:1px solid var(--line);display:flex;background:#fff}
.side .txt{width:150px;padding:20px 0 0 20px}
.side h4{font-size:17px;font-weight:600;line-height:1.25;color:#333;margin-bottom:10px}
.side p{font-size:10.5px;color:#888;line-height:1.5}
.side .ph{flex:1}
.btn-purple{background:var(--purple)}

/* blogs */
.blogs{height:1077px;position:relative}
.blogs h2{position:absolute;left:130px;top:10px;font-size:32px;color:var(--red);font-weight:400}
.feature{position:absolute;top:60px;width:305px;height:232px}
.feature .cap{position:absolute;left:0;right:0;bottom:0;height:56px;background:rgba(170,150,205,.92);color:#fff;font-size:17px;display:flex;align-items:center;justify-content:center}
.post{position:absolute;top:337px;width:227px}
.post .ph{height:132px;position:relative}
.date{position:absolute;left:0;bottom:0;width:44px;height:48px;background:var(--teal-dark);color:#fff;text-align:center;font-size:18px;line-height:1;padding-top:7px}
.date small{display:block;font-size:9px;margin-top:3px}
.post h5{font-size:13px;font-weight:400;margin:8px 0 4px}
.post p{font-size:9.5px;color:#999;line-height:1.45}
.more{font-size:10px;color:var(--teal-dark);margin-top:4px;display:block}
.mini{position:absolute;width:305px;height:112px;display:flex;gap:14px}
.mini .ph{width:145px;height:108px;flex:none}
.mini h5{font-size:14px;font-weight:400;line-height:1.3;color:#333;margin-top:6px}

/* footer */
.footer{position:absolute;top:3995px;left:0;right:0;height:297px;border-top:1px solid var(--line);background:#fff}
.footer .brand{position:absolute;left:130px;top:85px}
.fcol{position:absolute;top:65px;font-size:13px;color:#666}
.fcol h6{font-size:15px;color:var(--teal-dark);font-weight:700;margin-bottom:10px}
.fcol a{display:block;line-height:2.15}
.socials{display:flex;gap:8px;margin-top:8px}
.socials i{width:28px;height:28px;border-radius:50%;background:var(--teal-dark)}
.copy{position:absolute;top:4292px;left:0;right:0;height:77px;background:var(--bar);text-align:center;font-size:12px;color:#777;line-height:77px}
</style>
</head>
<body>

<div class="topbar">
  <div class="wrap">
    <a href="#">Join Our Associate Program »</a>
    <nav class="toplinks"><a href="#">Home</a><a href="#">Cart</a><a href="#">Blog</a><a href="#">Resources</a><a href="#">Contact</a></nav>
  </div>
</div>

<header class="header">
  <div class="wrap">
    <div class="brand">
      <span class="brand-dot"></span>
      <div class="brand-name">The Luma Haven</div>
    </div>
    <div class="search">
      <svg width="14" height="14" viewBox="0 0 14 14"><circle cx="6" cy="6" r="4.5" fill="none" stroke="#999" stroke-width="1.5"/><line x1="9.5" y1="9.5" x2="13" y2="13" stroke="#999" stroke-width="1.5"/></svg>
      Search here
    </div>
    <div class="callus">
      <small>Call Us Now</small>
      <b><svg width="22" height="22" viewBox="0 0 24 24"><path d="M6.6 10.8a15 15 0 0 0 6.6 6.6l2.2-2.2a1 1 0 0 1 1-.25 11.4 11.4 0 0 0 3.6.57 1 1 0 0 1 1 1V20a1 1 0 0 1-1 1A17 17 0 0 1 3 4a1 1 0 0 1 1-1h3.5a1 1 0 0 1 1 1c0 1.25.2 2.45.57 3.570a1 1 0 0 1-.25 1z" fill="none" stroke="#ec1f27" stroke-width="1.8"/></svg>1300 555 018</b>
    </div>
  </div>
</header>

<nav class="nav">
  <div class="wrap">
    <a href="#">Counselling<br>Types</a>
    <a href="#">Relationship Counselling<br>Locations</a>
    <a href="#">Sex Therapy<br>Locations</a>
    <a href="#">About Us</a>
    <a href="#">Quizzes</a>
    <a href="#">FAQ's</a>
    <a href="#">Contact</a>
  </div>
</nav>

<section class="hero" role="img" aria-label="Photo of a smiling couple lying together on grass">
  <h1 class="hero-title">RELATIONSHIP &amp;<br>MARRIAGE COUNSELLING</h1>
  <form class="finder">
    <h3>Find Our Psychologist<br>Near You</h3>
    <label>Type of Counselling</label>
    <div class="field"><span>Select</span><span>▾</span></div>
    <label>Location</label>
    <div class="field"></div>
    <label>Postcode</label>
    <div class="field"></div>
    <div class="go">SEARCH</div>
  </form>
  <div class="dots"><i></i><i></i><i></i><i></i></div>
</section>

<section class="intro">
  <div class="video" role="img" aria-label="Video still of a psychologist speaking">
    <svg width="70" height="70" viewBox="0 0 70 70"><circle cx="35" cy="35" r="32" fill="none" stroke="#fff" stroke-width="3"/><path d="M28 22 L50 35 L28 48Z" fill="#fff"/></svg>
  </div>
  <div class="intro-text">
    <h2>We Specialise in Relationship<br>&amp; Marriage Counselling</h2>
    <p>At Luma Haven, we are a group of PSYCHOLOGISTS, Australia wide who are passionate about relationships and helping you with yours. Our vision is to provide the most highly regarded and comprehensive marriage counselling and relationship counselling, and sex therapy in Australia, at reasonable and affordable rates.</p>
  </div>
  <div class="divider"><svg width="30" height="14" viewBox="0 0 30 14"><path d="M0 0 L15 13 L30 0" fill="#fff" stroke="#e3e3e3"/></svg></div>
</section>

<section class="services">
  <div class="wrap">
    <div class="cards">
      <article class="card">
        <div class="ph" role="img" aria-label="Photo of a couple talking" style="background:linear-gradient(135deg,#e4d2c4,#b79c8c)"></div>
        <div class="body"><h4 class="h-purple">Relationship<br>Counselling</h4><p>Communication, recovering from an affair, loss of intimacy and trust, power battles, parenting.</p><a class="btn" style="background:var(--purple)">Learn More</a></div>
      </article>
      <article class="card">
        <div class="ph" role="img" aria-label="Photo of a couple's feet in bed" style="background:linear-gradient(135deg,#f1e4dc,#cdb3a6)"></div>
        <div class="body"><h4 class="h-red">Sex Therapy<br>Counselling</h4><p>Low libido, female difficulties, premature ejaculation, differing desires, pain and arousal.</p><a class="btn" style="background:var(--red)">Learn More</a></div>
      </article>
      <article class="card">
        <div class="ph" role="img" aria-label="Photo of an arguing couple" style="background:linear-gradient(135deg,#c8d3db,#8f9aa3)"></div>
        <div class="body"><h4 style="color:var(--green)">Anger Management<br>Counselling</h4><p>Managing angry outbursts, expressing your anger in healthy ways.</p><a class="btn" style="background:var(--green)">Learn More</a></div>
      </article>
      <article class="card">
        <div class="ph" role="img" aria-label="Photo of a tense couple" style="background:linear-gradient(135deg,#b8a295,#6d5a50)"></div>
        <div class="body"><h4 class="h-teal">Narcissism<br>Counselling</h4><p>Managing narcissistic, superior, entitled, arrogant and lack of empathy tendencies.</p><a class="btn" style="background:var(--teal-dark)">Learn More</a></div>
      </article>
    </div>
  </div>
</section>

<section class="band">
  <div class="band-photo" role="img" aria-label="Photo of a happy older couple by the sea"></div>
  <h2>Our Luma Relationship Psychologists</h2>
  <div class="sub">Here are some of the common ones:</div>
  <ul style="left:130px">
    <li>Affairs</li><li>Controlling behaviour</li><li>Verbal abuse</li><li>Imbalance of power</li><li>Lack of intimacy</li><li>Poor communication</li><li>Loss of love</li>
  </ul>
  <ul style="left:405px">
    <li>Relationship neglect</li><li>Sexual problems</li><li>Problems from childhood</li><li>Problems with parenting your children</li><li>Step children and in-laws</li><li>All forms of family problems</li><li>Anger management problems</li>
  </ul>
</section>

<section class="approach">
  <div class="col-main">
    <h2 class="h-red">Our Relationship Counselling Approach</h2>
    <p>It is an important part of our policy to take a very positive approach to our relationship counselling. We feel it is important to really understand the problems and perspectives of each of you, and at the same time, we find that most couples are looking to find a positive action plan and way through their problems to make changes which have a positive impact and a real sense of hope for their relationship.</p>
    <p>Read more about our approach to counselling in our relationship counselling sessions, and frequently asked questions about the relationship and marriage counselling process.</p>
    <h2 class="h-purple" style="margin-top:44px">Our Relationship Counselling<br>Locations across Australia</h2>
    <p>We currently have relationship counselling and marriage counselling services in:</p>
    <div class="loc">
      <span>Sydney – 19 centres</span><span>Wollongong – 5 centre</span><span>Sunshine Coast – 2 centres</span>
      <span>Canberra – 2 centres</span><span>Central Coast – 2 centres</span><span>Cairns – 1 centre</span>
      <span>Melbourne – 21 centres</span><span>Adelaide – 4 centres</span><span>Townsville – 1 centre</span>
      <span>Perth – 11 centres</span><span>Gold Coast – 5 centres</span><span>Wodonga – 1 centre</span>
      <span>Brisbane – 14 centres</span>
    </div>
    <h2 class="h-teal">Communication is a vital skill but not<br>often taught to us.</h2>
    <p>Most people find that their ways of communicating with each other are what hamper us from having a happy healthy relationship.</p>
    <p>Effective Interpersonal Communication skills are not something that we are usually taught. But for almost everyone who is having difficulties in their relationship, they feel that they are trying to communicate their thoughts and feelings but that their partner is not listening.</p>
  </div>

  <aside class="side" style="top:42px">
    <div class="txt"><h4>Rebates<br>Available</h4><p>Simple support with fees for many sessions. Ask us how rebates apply.</p><a class="btn btn-purple">Learn More</a></div>
    <div class="ph" role="img" aria-label="Photo of a couple silhouetted at sunset" style="background:linear-gradient(160deg,#f6c9a8,#d97b8d 60%,#6b4a6a)"></div>
  </aside>
  <aside class="side" style="top:298px">
    <div class="txt"><h4>GP Referral<br>Info</h4><p>How a doctor referral works and what you need to bring along.</p><a class="btn btn-purple">Learn More</a></div>
    <div class="ph" role="img" aria-label="Photo of a couple embracing" style="background:linear-gradient(160deg,#d9c1ad,#8f7260)"></div>
  </aside>
  <aside class="side" style="top:560px">
    <div class="txt"><h4>Anxiety and<br>Depression</h4><p>Support for low mood and worry that strains a close relationship.</p><a class="btn btn-purple">Learn More</a></div>
    <div class="ph" role="img" aria-label="Photo of a thoughtful man" style="background:linear-gradient(160deg,#c9c3bd,#6f6660)"></div>
  </aside>
</section>

<section class="blogs">
  <h2>Latest Blogs</h2>
  <div class="feature" style="left:132px" role="img" aria-label="Photo of an upset woman">
    <div style="position:absolute;inset:0;background:linear-gradient(135deg,#e3cdbf,#a3877a)"></div>
    <div class="cap">How to Deal with an Affair?</div>
  </div>
  <div class="feature" style="left:450px" role="img" aria-label="Photo of two men talking">
    <div style="position:absolute;inset:0;background:linear-gradient(135deg,#cfc0b2,#6f5c50)"></div>
    <div class="cap">Same Sex Relationship</div>
  </div>
  <div class="feature" style="left:767px" role="img" aria-label="Photo of a man with his head in his hands">
    <div style="position:absolute;inset:0;background:linear-gradient(135deg,#d7cbc2,#4d4540)"></div>
    <div class="cap">Are You living with a narcissist?</div>
  </div>

  <article class="post" style="left:132px"><div class="ph" role="img" aria-label="Photo of a worried woman" style="background:linear-gradient(135deg,#e1d2c5,#a38d7d)"><div class="date">15<small>APR</small></div></div><h5>Your Blog Title here</h5><p>Short note on this topic for couples, with simple steps to try at home this week together.</p><a class="more">Read More</a></article>
  <article class="post" style="left:370px"><div class="ph" role="img" aria-label="Photo of a couple apart" style="background:linear-gradient(135deg,#9b8c80,#3f3732)"><div class="date">18<small>APR</small></div></div><h5>Your Blog Title here</h5><p>Short note on this topic for couples, with simple steps to try at home this week together.</p><a class="more">Read More</a></article>
  <article class="post" style="left:608px"><div class="ph" role="img" aria-label="Photo of a couple in discussion" style="background:linear-gradient(135deg,#bfb2a6,#6b5e55)"><div class="date">16<small>APR</small></div></div><h5>Your Blog Title here</h5><p>Short note on this topic for couples, with simple steps to try at home this week together.</p><a class="more">Read More</a></article>
  <article class="post" style="left:846px"><div class="ph" role="img" aria-label="Photo of a couple at sunset" style="background:linear-gradient(160deg,#f5b56c,#d9734a 60%,#5a3a3a)"><div class="date">05<small>APR</small></div></div><h5>Your Blog Title here</h5><p>Short note on this topic for couples, with simple steps to try at home this week together.</p><a class="more">Read More</a></article>

  <div class="mini" style="left:132px;top:562px"><div class="ph" role="img" aria-label="Photo of an arguing couple" style="background:linear-gradient(135deg,#b9a79a,#5e5048)"></div><div><h5>What can I do if I'm Living with a Narcissist?</h5><a class="more">Read More</a></div></div>
  <div class="mini" style="left:450px;top:562px"><div class="ph" role="img" aria-label="Photo of a sad couple" style="background:linear-gradient(135deg,#d2c3b6,#8a786b)"></div><div><h5>Why am I with a Narcissist?</h5><a class="more">Read More</a></div></div>
  <div class="mini" style="left:767px;top:562px"><div class="ph" role="img" aria-label="Photo of a couple arguing" style="background:linear-gradient(135deg,#d8b8a4,#8b5a48)"></div><div><h5>How Do I Know If I'm With a Narcissist?</h5><a class="more">Read More</a></div></div>

  <div class="mini" style="left:132px;top:690px"><div class="ph" role="img" aria-label="Photo of a couple in conflict" style="background:linear-gradient(135deg,#c6b5a8,#6e5f55)"></div><div><h5>Are You Living With a Steamroller?</h5><a class="more">Read More</a></div></div>
  <div class="mini" style="left:450px;top:690px"><div class="ph" role="img" aria-label="Photo of a couple holding hands" style="background:linear-gradient(135deg,#e2d4c8,#a4907f)"></div><div><h5>Letter for a Partner Doubtful About Relationship Counselling</h5><a class="more">Read More</a></div></div>
  <div class="mini" style="left:767px;top:690px"><div class="ph" role="img" aria-label="Photo of a smiling couple" style="background:linear-gradient(135deg,#e6c9b4,#b07e68)"></div><div><h5>Do You Wonder Why You and Your Partner Are Together?</h5><a class="more">Read More</a></div></div>

  <div class="mini" style="left:132px;top:815px"><div class="ph" role="img" aria-label="Photo of a couple talking on a sofa" style="background:linear-gradient(135deg,#c9bcb0,#75675c)"></div><div><h5>Did Your Relationship Start on Rocky Ground?</h5><a class="more">Read More</a></div></div>
  <div class="mini" style="left:450px;top:815px"><div class="ph" role="img" aria-label="Photo of a couple's hands" style="background:linear-gradient(135deg,#eadbd0,#b9a08f)"></div><div><h5>What Are You Like in a Relationship?</h5><a class="more">Read More</a></div></div>
  <div class="mini" style="left:767px;top:815px"><div class="ph" role="img" aria-label="Photo of a couple at sunset" style="background:linear-gradient(160deg,#f4b15f,#c9623e 60%,#4b2f2f)"></div><div><h5>Is Your Pursuit of Success Sabotaging Your Relationships That Matter Most?</h5><a class="more">Read More</a></div></div>
</section>

<footer class="footer">
  <div class="brand">
    <span class="brand-dot"></span>
    <div class="brand-name">The Luma Haven</div>
  </div>
  <div class="fcol" style="left:453px"><h6>QUICK LINKS</h6><a>Home</a><a>About Us</a><a>Our Blogs</a><a>Shop Cart</a><a>Contact Us</a></div>
  <div class="fcol" style="left:620px"><h6>RESOURCES</h6><a>Counselling Type</a><a>Sex Therapy</a><a>Quizzes</a><a>FAQ</a><a>Relationship Counselling</a></div>
  <div class="fcol" style="left:827px"><h6>CONTACT US</h6><a>12 Harbour Lane Suite 4</a><a>1300 555 018</a><a>Email: info@lumahaven.com.au</a><div class="socials"><i></i><i></i><i></i><i></i></div></div>
</footer>
<div class="copy">© 2017 Company Name. All right reserved</div>

</body>
</html>
```